Industrial Company Website

We need a Website to highlight 5 different Brands we distribute.

We are Dealers for the following products

1)Vantage Tube a Div of Harlow Bexton ( HDPE Pipes and Fittings )
Vantage Tube is the largest provider of polyethylene pipe (poly pipe) - HDPE pressure pipe and fittings in North America
Inquire page for web user to request pricing.

2) Dunstan Weldline Mfg . ( HDPE Fusion Equipment )'
We like to have a system we are able to list top 25 items with part numbers and cost
that a web user is able to select and add to cart and email a order via the web.

3) Heron Power ( Gate , Check and Globe Valves )
Sub Category Brands , Tightrun , BiStop , and Midaxis Valves

4) Taverno North America Valves
http://www.tavernonorthamerica-example.com/ita/home.pag

5) Corwell Strainers, Inc. - A worldwide manufacturer of heavy-duty air, lube, fuel, coolant, transmission, and hydraulic filtration products
Within this Tab we like to web user to lookup filters from
http://catalog.corwellstrainer-example.com/ and able to create a inquire
for our company to send a quote .

6) Hargreave-Tollan Uniforms
http://www.tollanwear-example.com/
http://www.blazeguard-example.com/fireservice/

http://www.ridgeforttreads-example.com/ (Safety Shoes)

Also we like a Tab for Company Profile , and contact information

We have authorization from all companies listed about to use their logo
under our dealership agreements.
Updates

Hello All ,

Please do not use the Varnel Oil & Gas Logo.

Please Only use the Logo with the Logo with the M and the Flame and Oil Drop

Ned                                   

Target Market(s)

Target Markets ,: International distributor of pipe, valves, fittings and more
serving the Caribbean and South America .

Target Clients : Oil and Gas , Power Plants and Mining Companies

The Web Address will be www.varnelsupply-example.com

Industry/Entity Type

It Company

Requirements
Must have
• Note : This Project will possibly lead to the next stage.
Coded and HTML proof of concept to load live.
I will give the winner first chance to Quote me the completion

Note the Goal is to have a E-Comm. Site , but since we are in Wholesale
and not retail . The E-Cart will no take payment but create an inquire and then send me to my email for processing
Nice to have
• I just had a Logo created by a designer on Sketch hive. I will need to share the logo design for your submission

```html
<!DOCTYPE html>
<html lang="en">
<head>
<meta charset="utf-8">
<title>Corvane International — Pipe, Valves &amp; Fittings</title>
<link rel="stylesheet" href="https://fonts.googleapis.com/css2?family=Oswald:wght@300;400;500&family=Open+Sans:wght@400;600&family=Tinos:ital,wght@0,400;0,700;1,700&display=swap">
<style>
:root{
  --brand-red:#8b1a0e;
  --ink:#222;
  --line:#ddd;
  --bar-black:#111;
  --sidebar-head:#8e8e8e;
  --white:#fff;
  --sky:#5f95cf;
  --sky-light:#a7c8e6;
  --pipe:#24262c;
  --machine-green:#3c6b48;
  --dirt:#b99a74;
  --poly-black:#2b2c30;
  --poly-grey:#5a5c62;
}
*{box-sizing:border-box;margin:0;padding:0}
html,body{width:1200px;height:2211px;overflow:hidden;background:var(--white)}
body{position:relative;font-family:"Open Sans",Arial,sans-serif;color:var(--ink)}
.abs{position:absolute}

/* utility bar */
.utility-bar{left:0;top:0;width:1200px;height:43px;background:var(--brand-red)}
.utility-bar a{position:absolute;top:0;height:43px;line-height:43px;color:var(--white);font:400 15px "Oswald",sans-serif;text-decoration:none;padding:0 10px;border-left:1px solid rgba(255,255,255,.55)}
.utility-bar a.edge{border-right:1px solid rgba(255,255,255,.55)}

/* header */
.brand{left:142px;top:88px;display:flex;align-items:center;gap:10px}
.brand-mark{width:26px;height:26px;border-radius:50%;background:var(--brand-red)}
.brand-name{font:500 20px "Oswald",sans-serif;color:var(--brand-red);line-height:1.05}
.search{left:771px;top:103px;width:288px;height:37px;border:1px solid var(--line);background:#f7f7f7;font:italic 12px "Open Sans",sans-serif;color:#999;padding:10px 14px}
.search svg{position:absolute;right:10px;top:9px}
.cart-btn{left:950px;top:150px;width:105px;height:24px;background:var(--brand-red);color:var(--white);font:600 10px "Open Sans",sans-serif;text-align:center;line-height:24px}

/* nav */
.main-nav{left:107px;top:189px;width:982px;height:49px;border:1px solid var(--line);background:linear-gradient(#fff,#f5f5f5);box-shadow:0 1px 3px rgba(0,0,0,.08)}
.main-nav span{position:absolute;top:13px;font:400 16px "Tinos",serif;color:#b3b3b3;letter-spacing:.5px}
.main-nav .active{color:var(--brand-red);border-bottom:2px solid var(--brand-red);padding-bottom:2px}

/* hero */
.hero{left:0;top:244px;width:1200px;height:650px;
  background:
    linear-gradient(180deg,rgba(0,0,0,0) 72%,var(--dirt) 88%),
    linear-gradient(100deg,var(--pipe) 0%,#3a3d45 30%,var(--machine-green) 58%,var(--sky) 78%,var(--sky-light) 100%);}
.hero-tab{top:248px;width:81px;height:23px;background:var(--brand-red);color:var(--white);font:400 13px "Oswald",sans-serif;text-align:center;line-height:23px}
.hero-caption{left:131px;top:556px;width:606px;height:103px;background:rgba(0,0,0,.55);color:var(--white);font:700 19px/1.45 "Tinos",serif;padding:22px 20px}
.hero-arrow{top:573px}

/* welcome */
.welcome-line1{left:131px;top:924px;font:400 30px "Tinos",serif;color:var(--ink)}
.welcome-line2{left:146px;top:970px;font:400 30px "Tinos",serif;color:var(--brand-red)}
.welcome-quote{left:357px;top:931px;font:300 14px/21px "Oswald",sans-serif;color:#444}
.read-more{left:855px;top:983px;width:97px;height:35px;background:var(--brand-red);border:3px solid #d9d9d9;color:var(--white);font:400 11px "Oswald",sans-serif;text-align:center;line-height:29px}

/* section headings */
.section-title{font:700 22px "Tinos",serif;color:var(--brand-red);letter-spacing:1px}
.rule{height:2px;background:linear-gradient(90deg,#e6e6e6,#f3f3f3)}
.pager-pill{left:956px;top:1036px;width:103px;height:31px;border-radius:16px;background:var(--bar-black)}

/* product cards */
.product-card{top:1094px;width:218px;height:313px;border:1px solid #d0d0d0;background:var(--white)}
.product-card .photo{position:absolute;left:18px;top:70px;width:180px;height:180px;border-radius:6px;background:linear-gradient(160deg,var(--poly-grey) 0%,var(--poly-black) 100%)}
.tag-new{position:absolute;right:0;top:10px;width:62px;height:22px;color:var(--white);font:400 13px "Oswald",sans-serif;text-align:center;line-height:22px;clip-path:polygon(14px 0,100% 0,100% 100%,0 100%)}
.product-meta{font:300 14px "Oswald",sans-serif;color:#444;line-height:25px}
.product-meta b{font-weight:300;color:var(--brand-red)}
.product-meta .name{color:var(--brand-red);font-weight:300;font-size:15px}

/* sidebar */
.sidebar{left:133px;top:1524px;width:187px;height:484px;border:1px solid #ccc}
.sidebar-head{height:33px;background:var(--sidebar-head);color:var(--white);font:400 14px "Oswald",sans-serif;line-height:33px;padding-left:14px;position:relative}
.sidebar-head i{position:absolute;right:0;top:0;width:33px;height:33px;background:#2b2b2b}
.sidebar-search{margin:9px 8px 0;height:30px;border:1px solid #ccc;font:italic 11px "Open Sans",sans-serif;color:#999;padding:7px 10px;position:relative}
.sidebar-list{position:absolute;left:9px;top:91px;list-style:none;font:400 12px "Open Sans",sans-serif;color:#333}
.sidebar-list li{height:23.4px}
.scroll-track{left:304px;top:1615px;width:4px;height:350px;background:#eee}
.scroll-thumb{left:304px;top:1667px;width:4px;height:30px;background:var(--brand-red)}

/* featured */
.page-dots{left:876px;top:1553px;display:flex;gap:7px}
.page-dots span{width:21px;height:21px;border:1px solid #bbb;font:11px "Open Sans",sans-serif;text-align:center;line-height:19px;color:#444}
.page-dots .on{background:var(--bar-black);color:var(--white);border-color:var(--bar-black)}
.feat-item{width:148px;text-align:center}
.feat-item .frame{height:114px;border:1px solid #bbb;padding:10px 14px;background:var(--white)}
.feat-item .fill{width:100%;height:100%;border-radius:4px}
.feat-item p{font:300 12px/21px "Oswald",sans-serif;color:#444}
.feat-item p.price{margin-top:12px}
.feat-item p span{color:var(--brand-red)}
.feat-item p.tag{font-size:11px}
.feat-item p.tag span{color:#999}
.feat-item p.name{color:var(--brand-red);font-size:11px}

/* footer */
.footer-rule{left:0;top:2035px;width:1200px;height:1px;background:#ccc}
.footer-col h4{font:400 12px "Oswald",sans-serif;color:#555;letter-spacing:.5px;margin-bottom:16px}
.footer-col li{list-style:none;font:400 11px/21px "Open Sans",sans-serif;color:#555}
.footer-col li::before{content:"» ";color:#888}
.footer-col .note{font:400 11px "Open Sans",sans-serif;color:#777}
.email-field{left:638px;top:2101px;width:113px;height:26px;border:1px solid #ccc;font:italic 10px "Open Sans",sans-serif;color:#aaa;padding:6px}
.subscribe{left:755px;top:2101px;width:70px;height:26px;background:#3d3d3d;color:var(--white);font:400 11px "Open Sans",sans-serif;text-align:center;line-height:26px}
.social-dot{top:2084px;width:16px;height:16px;border-radius:50%;background:#444}

.bottom-bar{left:0;top:2168px;width:1200px;height:43px;background:var(--bar-black)}
.copyright{left:131px;top:2182px;font:400 11px "Oswald",sans-serif;color:#ddd}
.pay-card{top:2176px;width:36px;height:24px;border-radius:3px;background:#e9e9e9}
</style>
</head>
<body>

<nav class="abs utility-bar">
  <a style="left:133px">$ USD</a>
  <a class="edge" style="left:204px">ENGLISH</a>
  <a style="left:786px">WELCOME</a>
  <a style="left:879px">LOGIN</a>
  <a style="left:944px">SIGN UP</a>
  <a class="edge" style="left:1011px">HELP</a>
</nav>

<div class="abs brand">
  <span class="brand-mark"></span>
  <span class="brand-name">CORVANE<br>INTERNATIONAL</span>
</div>

<div class="abs search">Search line
  <svg width="18" height="18" viewBox="0 0 18 18"><circle cx="7.5" cy="7.5" r="5.5" fill="none" stroke="#222" stroke-width="2"/><line x1="11.5" y1="11.5" x2="16" y2="16" stroke="#222" stroke-width="2"/></svg>
</div>
<div class="abs cart-btn">VIEW YOUR CART</div>

<nav class="abs main-nav">
  <span class="active" style="left:29px">HOME</span>
  <span style="left:116px">ABOUT</span>
  <span style="left:210px">PRODUCTS</span>
  <span style="left:335px">FEATURED</span>
  <span style="left:466px">STORE</span>
  <span style="left:555px">CONTACT</span>
</nav>

<section class="abs hero" role="img" aria-label="Photo of a worker operating a large HDPE pipe fusion machine on a pipeline site under a blue sky"></section>
<div class="abs hero-tab" style="left:911px">CONTACT</div>
<div class="abs hero-tab" style="left:1001px">PROFILE</div>
<div class="abs hero-caption">"Neque porro quisquam est qui dolorem ipsum quia dolor sit amet, consectetur, adipisci velit..."</div>
<svg class="abs hero-arrow" style="left:22px" width="76" height="76" viewBox="0 0 76 76"><circle cx="38" cy="38" r="35" fill="rgba(0,0,0,.35)" stroke="#fff" stroke-width="3"/><path d="M44 26 L28 38 L44 50Z" fill="#fff"/></svg>
<svg class="abs hero-arrow" style="left:1112px" width="76" height="76" viewBox="0 0 76 76"><circle cx="38" cy="38" r="35" fill="rgba(255,255,255,.15)" stroke="#fff" stroke-width="3"/><path d="M32 26 L48 38 L32 50Z" fill="#fff"/></svg>

<h1 class="abs welcome-line1" style="font-weight:400">WELCOME TO</h1>
<h2 class="abs welcome-line2" style="font-weight:400">MY WEBSITE</h2>
<p class="abs welcome-quote">"Neque porro quisquam est qui dolorem ipsum quia dolor sit amet, consectetur, adipisci velit..."<br>"There is no one who loves pain itself, who seeks after it and wants to have it, simply because it is pain..."</p>
<div class="abs read-more">READ MORE</div>

<h3 class="abs section-title" style="left:133px;top:1038px">NEW PRODUCTS</h3>
<div class="abs rule" style="left:345px;top:1052px;width:600px"></div>
<div class="abs pager-pill">
  <svg width="103" height="31" viewBox="0 0 103 31"><path d="M33 9 L26 15.5 L33 22" fill="none" stroke="#fff" stroke-width="2.5"/><path d="M70 9 L77 15.5 L70 22" fill="none" stroke="#fff" stroke-width="2.5"/></svg>
</div>

<article class="abs product-card" style="left:133px"><div class="tag-new" style="background:#bdbdbd">NEW</div><div class="photo" role="img" aria-label="Photo of a hydraulic butt fusion machine" style="background:linear-gradient(160deg,#6d7076,#2f3136)"></div></article>
<article class="abs product-card" style="left:369px"><div class="tag-new" style="background:#1f4f8f">NEW</div><div class="photo" role="img" aria-label="Photo of black HDPE pipe fittings: couplers, elbow and tee"></div></article>
<article class="abs product-card" style="left:605px"><div class="tag-new" style="background:#e9c21a">NEW</div><div class="photo" role="img" aria-label="Photo of a black HDPE reducer fitting"></div></article>
<article class="abs product-card" style="left:841px"><div class="tag-new" style="background:var(--brand-red)">NEW</div><div class="photo" role="img" aria-label="Photo of a black HDPE saddle clamp with gasket"></div></article>

<div class="abs product-meta" style="left:136px;top:1412px">PRICE : <b>200 $</b><br>TAGS : LOREM IPSUM DOLOR<br><span class="name">HDPE PIPES FITTINGS</span></div>
<div class="abs product-meta" style="left:372px;top:1412px">PRICE : <b>200 $</b><br>TAGS : LOREM IPSUM DOLOR<br><span class="name">HDPE PIPES FITTINGS</span></div>
<div class="abs product-meta" style="left:608px;top:1412px">PRICE : <b>200 $</b><br>TAGS : LOREM IPSUM DOLOR<br><span class="name">HDPE PIPES FITTINGS</span></div>
<div class="abs product-meta" style="left:844px;top:1412px">PRICE : <b>200 $</b><br>TAGS : LOREM IPSUM DOLOR<br><span class="name">HDPE PIPES FITTINGS</span></div>

<aside class="abs sidebar">
  <div class="sidebar-head">SELECT CATEGORY<i><svg width="33" height="33" viewBox="0 0 33 33"><path d="M11 14 L22 14 L16.5 20Z" fill="#fff"/></svg></i></div>
  <div class="sidebar-search">Search By Brand
    <svg style="position:absolute;right:7px;top:7px" width="14" height="14" viewBox="0 0 14 14"><circle cx="6" cy="6" r="4.3" fill="none" stroke="#333" stroke-width="1.6"/><line x1="9" y1="9" x2="13" y2="13" stroke="#333" stroke-width="1.6"/></svg>
  </div>
  <ul class="sidebar-list">
    <li>Lorum ipsum</li><li>Lorum ipsum</li><li>Lorum ipsum</li><li>Lorum ipsum</li><li>Lorum ipsum</li><li>Lorum ipsum</li><li>Lorum ipsum</li><li>Lorum ipsum</li><li>Lorum ipsum</li><li>Lorum ipsum</li><li>Lorum ipsum</li><li>Lorum ipsum</li><li>Lorum ipsum</li><li>Lorum ipsum</li><li>Lorum ipsum</li>
  </ul>
</aside>
<div class="abs scroll-track"></div>
<div class="abs scroll-thumb"></div>

<h3 class="abs section-title" style="left:339px;top:1522px;font-weight:400">FEATURED PRODUCTS</h3>
<div class="abs rule" style="left:600px;top:1537px;width:459px"></div>
<div class="abs page-dots"><span class="on">1</span><span>2</span><span>3</span><span>4</span><span>5</span><span>&gt;</span></div>

<div class="abs feat-item" style="left:365px;top:1602px"><div class="frame"><div class="fill" role="img" aria-label="Photo of a fusion machine power unit" style="background:linear-gradient(160deg,#8a7a6e,#4a3f3a)"></div></div><p class="price">PRICE : <span>200 $</span></p><p class="tag">TAG: <span>LOREM IPSUM</span></p><p class="name">HDPE FUSION EQUIPMENT</p></div>
<div class="abs feat-item" style="left:542px;top:1602px"><div class="frame"><div class="fill" role="img" aria-label="Photo of a handheld socket fusion tool" style="background:linear-gradient(160deg,#d97a4a,#9a9ca0)"></div></div><p class="price">PRICE : <span>200 $</span></p><p class="tag">TAG: <span>LOREM IPSUM</span></p><p class="name">HDPE FUSION EQUIPMENT</p></div>
<div class="abs feat-item" style="left:722px;top:1602px"><div class="frame"><div class="fill" role="img" aria-label="Photo of a butt fusion machine with hydraulic unit" style="background:linear-gradient(160deg,#c73a2c,#555)"></div></div><p class="price">PRICE : <span>200 $</span></p><p class="tag">TAG: <span>LOREM IPSUM</span></p><p class="name">HDPE FUSION EQUIPMENT</p></div>
<div class="abs feat-item" style="left:880px;top:1602px"><div class="frame"><div class="fill" role="img" aria-label="Photo of a yellow and blue fusion machine on a stand" style="background:linear-gradient(180deg,#e8c12a,#2d5fa8)"></div></div><p class="price">PRICE : <span>200 $</span></p><p class="tag">TAG: <span>LOREM IPSUM</span></p><p class="name">HDPE FUSION EQUIPMENT</p></div>

<div class="abs feat-item" style="left:365px;top:1816px"><div class="frame"><div class="fill" role="img" aria-label="Photo of a green wheeled fusion unit" style="background:linear-gradient(160deg,#3f8a55,#1e3a28)"></div></div><p class="price">PRICE : <span>200 $</span></p><p class="tag">TAG: <span>LOREM IPSUM</span></p><p class="name">HDPE FUSION EQUIPMENT</p></div>
<div class="abs feat-item" style="left:542px;top:1816px"><div class="frame"><div class="fill" role="img" aria-label="Photo of a row of red oil filters" style="background:linear-gradient(160deg,#e0392a,#9c1c12)"></div></div><p class="price">PRICE : <span>200 $</span></p><p class="tag">TAG: <span>LOREM IPSUM</span></p><p class="name">HDPE FUSION EQUIPMENT</p></div>
<div class="abs feat-item" style="left:722px;top:1816px"><div class="frame"><div class="fill" role="img" aria-label="Photo of a red air filter element" style="background:linear-gradient(160deg,#d23a2a,#6b6b6b)"></div></div><p class="price">PRICE : <span>200 $</span></p><p class="tag">TAG: <span>LOREM IPSUM</span></p><p class="name">HDPE FUSION EQUIPMENT</p></div>
<div class="abs feat-item" style="left:880px;top:1816px"><div class="frame"><div class="fill" role="img" aria-label="Photo of a yellow and blue fusion machine on a stand" style="background:linear-gradient(180deg,#e8c12a,#2d5fa8)"></div></div><p class="price">PRICE : <span>200 $</span></p><p class="tag">TAG: <span>LOREM IPSUM</span></p><p class="name">HDPE FUSION EQUIPMENT</p></div>

<div class="abs footer-rule"></div>
<footer>
  <div class="abs footer-col" style="left:189px;top:2052px"><h4>SUPPORT</h4><ul><li>Our stores</li><li>Contact us</li><li>Sitemap</li></ul></div>
  <div class="abs footer-col" style="left:414px;top:2052px"><h4>CATALOG</h4><ul><li>Specials</li><li>New products</li><li>Top sellers</li></ul></div>
  <div class="abs footer-col" style="left:638px;top:2052px"><h4>NEWSLETTER</h4><p class="note">Subscribe to our newsletter</p></div>
  <div class="abs email-field">Your e-mail</div>
  <div class="abs subscribe">Subscribe</div>
  <div class="abs footer-col" style="left:864px;top:2052px"><h4>GET SOCIAL</h4></div>
  <span class="abs social-dot" style="left:869px"></span>
  <span class="abs social-dot" style="left:900px"></span>
  <span class="abs social-dot" style="left:931px"></span>
  <span class="abs social-dot" style="left:962px"></span>
</footer>

<div class="abs bottom-bar"></div>
<div class="abs copyright">COPY RIGHTS© 2013 . ALL RIGHTS RESERVED</div>
<span class="abs pay-card" style="left:847px"></span>
<span class="abs pay-card" style="left:887px"></span>
<span class="abs pay-card" style="left:927px"></span>
<span class="abs pay-card" style="left:967px"></span>
<span class="abs pay-card" style="left:1005px"></span>

</body>
</html>
```